Bramleys Tea Corner Website

I need a website for a diner/restaurant that has been established in a farming, oil and industrial community for over 15 years. The website needs to be simple in design, but that should demonstrate the mastery of skills of the designer. Our diner/restaurant is family oriented, patriotic but very rustic
Fb Address is fb.me/BramleysUSA

Pictures of the restaurant

https://www.filecrate.example/s/k3vq8wz1tn0x7rb/Bramleys_05.jpg?dl=0

Pictures of About us

https://www.filecrate.example/sh/qmt604z918wle27/BBBqk7HDvtQxa2Rnhy-KP8153c?dl=0

Article about Bramley's
https://www.filecrate.example/s/7h2r61xzuvmd40p/BramleysTeaCorner1.PDF?dl=0
https://www.filecrate.example/s/w8ky37lnqjbe91c/BramleysTeaCorner2.PDF?dl=0

Project Deadline Extended
Reason: I was slow to update with information.

Project Deadline Extended
Reason: I am just getting feedback to the designs posted. I wasn't sure of the limited feedback was limiting designers from submitting designs. That and running a business with 25 employees open 12 hours a day, being here 2 hours prior and 2-3 hours after makes for long days.

I've increased the first place prize and also added funds to the second and third place prizes for your effort.

I just need the files in PSD, not HTML 5 as originally requested. We can handle getting the coding part.

Ill have the contest finalized by Monday. Thanks for your patience.

Target Market(s)

Cross section of adults from 18-35 & 35-55.

Industry/Entity Type

Industrial

Font styles to use
Other font styles liked:
• ff tisa web pro or garamond premier pro

Requirements
Must have
• Must be clean, look nice and not look like an afterthought.
Nice to have
• Please see the last two documents for information about our restaurant, which was featured in our local newspaper.

```html
<!DOCTYPE html>
<html lang="en">
<head>
<meta charset="utf-8">
<title>Bramley's Breakfast Menu</title>
<link rel="stylesheet" href="https://fonts.googleapis.com/css2?family=Architects+Daughter&family=Cabin+Sketch:wght@700&family=Oswald:wght@500&display=swap">
<style>
  :root {
    --paper: #ececea;
    --board: #2b2b2b;
    --board-edge: #1f1f1f;
    --chalk: #f2f2f0;
    --chalk-soft: #d9d9d6;
    --likes-blue: #3c5e7c;
    --art-tone: #4a4a49;
  }
  html, body {
    margin: 0;
    padding: 0;
    width: 1115px;
    height: 1200px;
    overflow: hidden;
    background: var(--board);
  }
  .canvas {
    position: relative;
    width: 1200px;
    height: 1293px;
    transform: scale(0.928);
    transform-origin: 0 0;
    font-family: "Architects Daughter", cursive;
    color: var(--chalk);
    text-transform: uppercase;
  }
  .likes-bar {
    position: absolute;
    left: 0; top: 0;
    width: 1200px; height: 80px;
    background: var(--paper);
  }
  .likes-count {
    position: absolute;
    left: 534px; top: 20px;
    font-family: "Oswald", sans-serif;
    font-weight: 500;
    font-size: 24px;
    letter-spacing: -0.5px;
    color: var(--likes-blue);
  }
  .likes-mark {
    position: absolute;
    left: 646px; top: 20px;
    width: 26px; height: 26px;
    border: 3px solid var(--likes-blue);
    box-sizing: border-box;
  }
  .chalkboard {
    position: absolute;
    left: 0; top: 80px;
    width: 1200px; height: 1213px;
    background: radial-gradient(ellipse at 50% 40%, #343434 0%, var(--board) 55%, var(--board-edge) 100%);
  }
  .art {
    position: absolute;
    background: radial-gradient(ellipse at center, var(--art-tone) 0%, rgba(74,74,73,0.35) 60%, rgba(43,43,43,0) 100%);
    border-radius: 18px;
  }
  .art-breakfast { left: 40px; top: 135px; width: 400px; height: 365px; }
  .art-cutlery { left: 978px; top: 122px; width: 215px; height: 150px; }
  .art-hand { left: 790px; top: 1168px; width: 92px; height: 72px; }

  .menu-title {
    position: absolute;
    left: 0; top: 140px;
    width: 1200px;
    text-align: center;
    font-family: "Cabin Sketch", sans-serif;
    font-weight: 700;
    font-size: 70px;
    letter-spacing: 2px;
    line-height: 1;
    margin: 0;
  }
  .title-dashes {
    position: absolute;
    top: 152px;
  }
  .title-dashes.left { left: 344px; }
  .title-dashes.right { left: 796px; }
  .menu-subtitle {
    position: absolute;
    left: 0; top: 232px;
    width: 1200px;
    text-align: center;
    font-size: 24px;
    letter-spacing: 2px;
    margin: 0;
  }

  .item { position: absolute; }
  .col-left .item { left: 91px; width: 482px; }
  .col-right .item { left: 607px; width: 490px; }
  .item-name {
    font-size: 21px;
    line-height: 30px;
    white-space: nowrap;
  }
  .item-name small {
    font-size: 14px;
  }
  .item-desc {
    font-size: 12.5px;
    line-height: 22px;
    color: var(--chalk-soft);
    white-space: nowrap;
  }
  .item-plain {
    font-size: 14px;
    line-height: 30px;
    color: var(--chalk-soft);
  }
  .price {
    position: absolute;
    top: 0;
    font-size: 24px;
    line-height: 30px;
    color: var(--chalk-soft);
  }
  .col-left .price { right: 0; }
  .col-right .price { left: 425px; }
  .price-split {
    position: absolute;
    right: 4px;
    font-size: 23px;
    line-height: 30px;
    color: var(--chalk-soft);
  }
  .lunch-link {
    position: absolute;
    left: 407px; top: 1205px;
    font-size: 21px;
    letter-spacing: 1.5px;
    white-space: nowrap;
  }
</style>
</head>
<body>
<div class="canvas">
  <header class="likes-bar">
    <span class="likes-count">6,439 LIKES</span>
    <span class="likes-mark"></span>
  </header>

  <main class="chalkboard"></main>

  <div class="art art-breakfast" role="img" aria-label="Chalk drawing of a breakfast table: coffee cup, plate of fried eggs and bacon, toast and cutlery"></div>
  <div class="art art-cutlery" role="img" aria-label="Chalk drawing of knife, fork, spoon and a plate with a slice of pie"></div>

  <svg class="title-dashes left" width="40" height="50" viewBox="0 0 40 50">
    <g stroke="#f2f2f0" stroke-width="3" stroke-linecap="round">
      <line x1="10" y1="8" x2="36" y2="12"/>
      <line x1="4" y1="25" x2="36" y2="25"/>
      <line x1="10" y1="42" x2="36" y2="38"/>
    </g>
  </svg>
  <h1 class="menu-title">Breakfast</h1>
  <svg class="title-dashes right" width="40" height="50" viewBox="0 0 40 50">
    <g stroke="#f2f2f0" stroke-width="3" stroke-linecap="round">
      <line x1="4" y1="12" x2="30" y2="8"/>
      <line x1="4" y1="25" x2="36" y2="25"/>
      <line x1="4" y1="38" x2="30" y2="42"/>
    </g>
  </svg>
  <p class="menu-subtitle">Served all day</p>

  <section class="col-left">
    <div class="item" style="top:521px">
      <div class="item-name">The Sausage Patty</div>
      <div class="item-desc">Our original 8oz sausage patty with a spicy kick,<br>served with two eggs</div>
      <span class="price">8.89</span>
    </div>
    <div class="item" style="top:605px">
      <div class="item-name">Chicken Fried Steak</div>
      <div class="item-desc">(One of the biggest in town) with two eggs</div>
      <span class="price-split" style="top:0">Full-11.29</span>
      <span class="price-split" style="top:37px;right:10px">Half-8.99</span>
    </div>
    <div class="item" style="top:680px">
      <div class="item-name">Jumbo Ham Steak</div>
      <div class="item-desc">(One of the biggest in town) with two eggs</div>
      <span class="price">11.29</span>
    </div>
    <div class="item" style="top:740px">
      <div class="item-name">Steak and Eggs</div>
      <div class="item-desc">USDA prime 10oz rib-eye with two eggs, get ’em cowboy</div>
      <span class="price">11.29</span>
    </div>
    <div class="item" style="top:800px">
      <div class="item-name">All-American Breakfast</div>
      <div class="item-desc">Two eggs with 4 bacon or 2 sausage</div>
      <span class="price">8.79</span>
    </div>
    <div class="item" style="top:862px">
      <div class="item-plain">One egg with 2 bacon or 1 sausage</div>
      <span class="price">6.99</span>
    </div>
    <div class="item" style="top:898px">
      <div class="item-name">Corned Beef Hash <small>with two eggs</small></div>
      <span class="price">8.99</span>
    </div>
    <div class="item" style="top:935px">
      <div class="item-name">Migas</div>
      <div class="item-desc">Three corn tortillas fried until golden brown<br>and scrambled with two eggs</div>
      <span class="price">8.99</span>
    </div>
    <div class="item" style="top:1017px">
      <div class="item-name">Deluxe Scramble</div>
      <div class="item-desc">Ham, Mesa chiles, onions and cheese</div>
      <span class="price">8.99</span>
    </div>
    <div class="item" style="top:1078px">
      <div class="item-name">Meat Lovers Skillet</div>
      <div class="item-desc">Hot links, ham, sausage, bacon and jack cheese</div>
      <span class="price">9.79</span>
    </div>
  </section>

  <section class="col-right">
    <div class="item" style="top:303px">
      <div class="item-name">Veggie Omelet</div>
      <div class="item-desc">Onions, tomatoes, bell peppers, mushrooms<br>and broccoli</div>
      <span class="price">9.59</span>
    </div>
    <div class="item" style="top:386px">
      <div class="item-name">Sausage and Cheese Omelet</div>
      <span class="price">9.79</span>
    </div>
    <div class="item" style="top:424px">
      <div class="item-name">Bacon and Cheese Omelet</div>
      <span class="price">9.79</span>
    </div>
    <div class="item" style="top:462px">
      <div class="item-name">Bramley’s Omelet</div>
      <div class="item-desc">All meat and cheese</div>
      <span class="price">10.49</span>
    </div>
    <div class="item" style="top:522px">
      <div class="item-name">Spinach Omelet</div>
      <div class="item-desc">With fresh feta cheese, tomatoes, mushrooms and swiss cheese</div>
      <span class="price">9.79</span>
    </div>
    <div class="item" style="top:582px">
      <div class="item-name">Denver Omelet</div>
      <div class="item-desc">Ham, onions, bell peppers and cheese</div>
      <span class="price">9.69</span>
    </div>
    <div class="item" style="top:643px">
      <div class="item-name">Broccoli Omelet</div>
      <div class="item-desc">Broccoli, ham, mushrooms and jack cheese</div>
      <span class="price">9.79</span>
    </div>
    <div class="item" style="top:704px">
      <div class="item-name">Cowboy Benedict</div>
      <div class="item-desc">Two sausage patties on an open biscuit,<br>two poached eggs and gravy</div>
      <span class="price">9.79</span>
    </div>
    <div class="item" style="top:786px">
      <div class="item-name">Cheese Omelet</div>
      <span class="price">8.99</span>
    </div>
    <div class="item" style="top:824px">
      <div class="item-name">Ham and Cheese Omelet</div>
      <span class="price">9.79</span>
    </div>
    <div class="item" style="top:862px">
      <div class="item-name">Monterey Omelet</div>
      <div class="item-desc">Mesa chilies, ham and jack cheese</div>
      <span class="price">9.79</span>
    </div>
    <div class="item" style="top:922px">
      <div class="item-name">Snake Bite Omelet</div>
      <div class="item-desc">Polish sausage, pickled jalapenos,<br>yellow pepper rings and jack cheese</div>
      <span class="price" style="left:431px">10.19</span>
    </div>
    <div class="item" style="top:1004px">
      <div class="item-name">Hobo Omelet</div>
      <div class="item-desc">Bacon, ham, sausage, onions, tomatoes, bell peppers,<br>mushrooms and cheese</div>
      <span class="price" style="left:431px">10.49</span>
    </div>
    <div class="item" style="top:1087px">
      <div class="item-name">Harvest Omelet</div>
      <div class="item-desc">Sausage, bell peppers, onions and cheese</div>
      <span class="price">9.79</span>
    </div>
  </section>

  <div class="lunch-link">Bramley’s Hearty Lunches</div>
  <div class="art art-hand" role="img" aria-label="Chalk drawing of a hand pointing right toward the lunch menu"></div>
</div>
</body>
</html>
```